Video Performance Case study

We need to design a double sided stats sheet for the presentation of data relating to the performance of videos that we have marketed. Front page can be very image based and the back page should be info graphics based. A3 would probably work best but open to larger sizes if necessary. The data that we need to present is Geographical, number of views, completion rate (%), short overview of what we did, sample URL's.
This flyer will be used as a sales tool to highlight the work that we have done so needs to look very cool and modern.
Will be printed as a two sider and distributed online via PDF
Ideally will be produced in InDesign but Photoshop is OK.

```html
<!DOCTYPE html>
<html lang="en">
<head>
<meta charset="utf-8">
<title>Video Performance Case Study</title>
<link rel="stylesheet" href="https://fonts.googleapis.com/css2?family=Oswald:wght@400;500;600;700&family=Roboto+Condensed:wght@300;400&display=swap">
<style>
:root{
  --backdrop:#dcd9d3;
  --paper:#e8e7e2;
  --ink:#1b1b1b;
  --red:#d0202a;
  --map-light:#c9c9c6;
  --map-mid:#9d9d9b;
  --muted:#b9b8b4;
  --body:#4a4a4a;
}
*{margin:0;padding:0;box-sizing:border-box}
html,body{width:1200px;height:892px;overflow:hidden}
body{background:var(--backdrop);position:relative;font-family:"Roboto Condensed",Arial,sans-serif;color:var(--ink)}
.sheet{position:absolute;top:83px;width:514px;height:729px;background:var(--paper);box-shadow:0 2px 6px rgba(0,0,0,.18);overflow:hidden}
.sheet--front{left:62px}
.sheet--back{left:624px}
.abs{position:absolute}
.display{font-family:"Oswald",Arial,sans-serif;font-weight:600;text-transform:uppercase;line-height:1}

/* front */
.icon-cluster{left:34px;top:12px;width:445px;height:128px;background:linear-gradient(180deg,#d2d1cc,#c3c2bd);border-radius:4px}
.title-band{left:0;top:0;width:514px;height:320px}
.title-word{position:absolute;color:#fff;line-height:1;white-space:nowrap;font-family:"Oswald",Arial,sans-serif;text-transform:uppercase}
.title-word--lead{left:38px;top:173px;font-size:32px;font-weight:500;letter-spacing:.5px}
.title-word--videos{left:318px;top:153px;font-size:45px;font-weight:600;letter-spacing:1px}
.title-word--that{left:40px;top:203px;font-size:28px;font-weight:500;letter-spacing:.5px}
.title-word--marketed{left:250px;top:202px;font-size:53px;font-weight:600;letter-spacing:.5px}
.world-map{background:radial-gradient(ellipse at 50% 45%,var(--map-mid),var(--map-light) 70%,var(--paper) 100%);border-radius:40%/30%}
.front-map{left:20px;top:300px;width:477px;height:268px}
.views-label{left:39px;top:584px;font-size:14px;font-weight:500}
.completion{color:var(--red)}
.completion .small{font-size:15px;font-weight:500;display:block}
.completion .big{font-size:28px;font-weight:600;display:block;margin-top:2px}
.chart-svg text{font-family:"Oswald",Arial,sans-serif}

/* back */
.ribbon{left:17px;top:10px;width:275px;height:92px}
.ribbon-line{position:absolute;color:#fff;white-space:nowrap;line-height:1;font-family:"Oswald",Arial,sans-serif;text-transform:uppercase;font-weight:600}
.ribbon-line--one{left:38px;top:35px;font-size:22px;letter-spacing:1.5px}
.ribbon-line--two{left:38px;top:58px;font-size:18px;letter-spacing:1px}
.copy{font-size:9.6px;line-height:13.4px;color:var(--body);font-weight:300}
.intro{left:286px;top:18px;width:214px}
.heading{font-size:13px;font-weight:500;line-height:1.15}
.rule{height:1px;background:var(--red)}
.col{top:177px;width:86px}
.back-map{left:202px;top:134px;width:299px;height:182px}
.pointer{left:122px;top:341px;width:0;height:0;border-top:11px solid transparent;border-bottom:11px solid transparent;border-right:22px solid var(--ink)}
.www{left:18px;top:585px;font-size:34px;font-weight:700}
.urls-label{left:18px;top:622px;font-size:13px;font-weight:500}
.url-list{left:18px;top:657px;font-family:"Oswald",Arial,sans-serif;font-size:12.5px;font-weight:500;line-height:14.6px;list-style:none}
.extra-box{left:215px;top:584px;width:284px;height:131px;border:1px dashed #9a9a96;display:flex;align-items:center;justify-content:center;text-align:center;color:var(--muted);font-size:12.5px;font-weight:500}
</style>
</head>
<body>

<section class="sheet sheet--front">
  <div class="abs icon-cluster" role="img" aria-label="Cluster of black video and media icons: director chair, camera, reel, globe, target, clapperboard, tripod, TV, megaphone, microphone"></div>

  <svg class="abs title-band" viewBox="0 0 514 320" aria-hidden="true">
    <polygon points="0,150 514,116 514,302 0,254" fill="var(--ink)"/>
    <polygon points="0,164 514,132 514,286 0,240" fill="var(--red)"/>
    <line x1="0" y1="157" x2="514" y2="124" stroke="#fff" stroke-width="5" stroke-dasharray="4 4"/>
    <line x1="0" y1="247" x2="514" y2="294" stroke="#fff" stroke-width="6" stroke-dasharray="5 5"/>
  </svg>
  <h1 class="title-heading">
    <span class="title-word title-word--lead">Performance of</span>
    <span class="title-word title-word--videos">Videos</span>
    <span class="title-word title-word--that">That we have</span>
    <span class="title-word title-word--marketed">Marketed</span>
  </h1>

  <div class="abs world-map front-map" role="img" aria-label="Grey world map with North America, Greenland, Mexico, Brazil and China highlighted in black"></div>

  <svg class="abs" style="left:0;top:0" width="514" height="729" aria-hidden="true">
    <g font-family="Oswald, Arial, sans-serif" font-weight="600" font-size="14" fill="#fff" text-anchor="middle">
      <line x1="56" y1="308" x2="62" y2="318" stroke="var(--red)" stroke-width="2"/>
      <circle cx="44" cy="296" r="18" fill="var(--ink)" stroke="var(--red)" stroke-width="4"/><text x="44" y="301">5%</text>
      <circle cx="292" cy="339" r="18" fill="var(--ink)" stroke="var(--red)" stroke-width="4"/><text x="292" y="344">5%</text>
      <circle cx="472" cy="431" r="18" fill="var(--ink)" stroke="var(--red)" stroke-width="4"/><text x="472" y="436">25%</text>
      <circle cx="76" cy="472" r="18" fill="var(--ink)" stroke="var(--red)" stroke-width="4"/><text x="76" y="477">15%</text>
      <circle cx="198" cy="456" r="18" fill="var(--ink)" stroke="var(--red)" stroke-width="4"/><text x="198" y="461">25%</text>
      <circle cx="358" cy="502" r="18" fill="var(--ink)" stroke="var(--red)" stroke-width="4"/><text x="358" y="507">15%</text>
    </g>
  </svg>

  <p class="abs display views-label">Number of view</p>
  <svg class="abs" style="left:36px;top:606px" width="104" height="106" viewBox="0 0 104 106" role="img" aria-label="TV showing 70 percent">
    <path d="M36 4 L52 20 L68 4" fill="none" stroke="var(--ink)" stroke-width="6"/>
    <rect x="3" y="20" width="98" height="76" rx="16" fill="none" stroke="var(--ink)" stroke-width="7"/>
    <rect x="24" y="94" width="12" height="8" fill="var(--ink)"/><rect x="68" y="94" width="12" height="8" fill="var(--ink)"/>
    <text x="52" y="72" text-anchor="middle" font-family="Oswald, Arial, sans-serif" font-size="34" font-weight="500" fill="var(--red)">70%</text>
  </svg>

  <p class="abs display completion" style="left:189px;top:577px"><span class="small">Completion</span><span class="big">% Rate</span></p>

  <svg class="abs chart-svg" style="left:0;top:0" width="514" height="729" role="img" aria-label="Completion rate by month: 25, 5, 45, 30, 35">
    <line x1="178" y1="580" x2="178" y2="701" stroke="var(--ink)" stroke-width="1"/>
    <line x1="178" y1="701" x2="480" y2="701" stroke="var(--ink)" stroke-width="1"/>
    <g stroke="var(--ink)"><line x1="204" y1="697" x2="204" y2="701"/><line x1="230" y1="697" x2="230" y2="701"/><line x1="256" y1="697" x2="256" y2="701"/><line x1="282" y1="697" x2="282" y2="701"/><line x1="308" y1="697" x2="308" y2="701"/><line x1="334" y1="697" x2="334" y2="701"/><line x1="360" y1="697" x2="360" y2="701"/><line x1="386" y1="697" x2="386" y2="701"/><line x1="412" y1="697" x2="412" y2="701"/><line x1="438" y1="697" x2="438" y2="701"/><line x1="464" y1="697" x2="464" y2="701"/></g>
    <polyline points="178,673 236,646 284,680 338,581 377,634 430,609 478,632" fill="none" stroke="var(--ink)" stroke-width="1.3"/>
    <g font-size="12" font-weight="600" fill="#fff" text-anchor="middle">
      <circle cx="236" cy="646" r="11" fill="var(--ink)" stroke="var(--red)" stroke-width="3"/><text x="236" y="650">25</text>
      <circle cx="284" cy="680" r="11" fill="var(--ink)" stroke="var(--red)" stroke-width="3"/><text x="284" y="684">5</text>
      <circle cx="338" cy="581" r="11" fill="var(--ink)" stroke="var(--red)" stroke-width="3"/><text x="338" y="585">45</text>
      <circle cx="377" cy="634" r="11" fill="var(--ink)" stroke="var(--red)" stroke-width="3"/><text x="377" y="638">30</text>
      <circle cx="430" cy="609" r="11" fill="var(--ink)" stroke="var(--red)" stroke-width="3"/><text x="430" y="613">35</text>
    </g>
    <g font-size="6.5" fill="var(--ink)" text-anchor="middle">
      <text x="183" y="711">JAN</text><text x="208" y="711">FEB</text><text x="236" y="711">MAR</text><text x="261" y="711">APR</text><text x="288" y="711">MAY</text><text x="314" y="711">JUN</text><text x="340" y="711">JUL</text><text x="366" y="711">AUG</text><text x="392" y="711">SEP</text><text x="418" y="711">OCT</text><text x="444" y="711">NOV</text><text x="470" y="711">DEC</text>
    </g>
  </svg>
</section>

<section class="sheet sheet--back">
  <svg class="abs ribbon" viewBox="0 0 275 92" aria-hidden="true">
    <polygon points="0,10 250,18 275,46 250,76 0,92" fill="var(--ink)"/>
    <line x1="4" y1="16" x2="246" y2="24" stroke="#fff" stroke-width="4" stroke-dasharray="4 4"/>
    <line x1="4" y1="86" x2="246" y2="70" stroke="#fff" stroke-width="4" stroke-dasharray="4 4"/>
  </svg>
  <h2 class="ribbon-heading">
    <span class="ribbon-line ribbon-line--one">Doutamas magnihi</span>
    <span class="ribbon-line ribbon-line--two">Etaut reius tempor</span>
  </h2>

  <p class="abs copy intro">Hicienec uptaqui aectam acepra sunt officia lumquis dolecae comnis untus demquia nes rehentem repeo volese eicidername net, consed mi, tem asimporeiur alistint apicitia porerum quid mi, corporiati aceatnate voloratum etur accum ut is sectem expedisdolo mvo lese eicidername net, consed mi, temeraiste astsim imporeiur. net, consed mi, tem asimporeiur.</p>

  <h3 class="abs display heading" style="left:18px;top:131px">Doluptam as magnihi<br>cabore re nonse plitius</h3>
  <div class="abs rule" style="left:18px;top:164px;width:150px"></div>
  <p class="abs copy col" style="left:18px">Hicienec uptaqui aectam acepra sunt officia dolumquis dolecae comnis untus demquia nes rehentem reperro volese eicidername net, consed mi, tem asimporeiur porerum quid mi, corporiati aceaten dollecaes.</p>
  <p class="abs copy col" style="left:109px">Hicienec uptaqui aectam acepra sunt officia dolumquis dolecae comnis untus demquia nes rehentem reperro volese eicidername net, consed mi, tem asimporeiur alistint apicitia porerum quid mi, corporiati untus.</p>

  <div class="abs world-map back-map" role="img" aria-label="Grey world map with Alaska, Greenland, Mexico, Brazil and China highlighted in black"></div>
  <svg class="abs" style="left:0;top:0" width="514" height="729" aria-hidden="true">
    <g font-family="Oswald, Arial, sans-serif" font-weight="600" font-size="10" fill="#fff" text-anchor="middle">
      <circle cx="211" cy="146" r="12" fill="var(--ink)" stroke="var(--red)" stroke-width="3"/><text x="211" y="150">5%</text>
      <circle cx="351" cy="171" r="12" fill="var(--ink)" stroke="var(--red)" stroke-width="3"/><text x="351" y="175">5%</text>
      <circle cx="484" cy="228" r="12" fill="var(--ink)" stroke="var(--red)" stroke-width="3"/><text x="484" y="232">25%</text>
      <circle cx="237" cy="254" r="12" fill="var(--ink)" stroke="var(--red)" stroke-width="3"/><text x="237" y="258">15%</text>
      <circle cx="313" cy="244" r="12" fill="var(--ink)" stroke="var(--red)" stroke-width="3"/><text x="313" y="248">25%</text>
      <circle cx="413" cy="273" r="12" fill="var(--ink)" stroke="var(--red)" stroke-width="3"/><text x="413" y="277">15%</text>
    </g>
  </svg>

  <svg class="abs" style="left:18px;top:329px" width="90" height="94" viewBox="0 0 104 106" role="img" aria-label="TV showing 70 percent">
    <path d="M36 4 L52 20 L68 4" fill="none" stroke="var(--ink)" stroke-width="6"/>
    <rect x="3" y="20" width="98" height="76" rx="16" fill="none" stroke="var(--ink)" stroke-width="7"/>
    <rect x="24" y="94" width="12" height="8" fill="var(--ink)"/><rect x="68" y="94" width="12" height="8" fill="var(--ink)"/>
    <text x="52" y="72" text-anchor="middle" font-family="Oswald, Arial, sans-serif" font-size="34" font-weight="500" fill="var(--red)">70%</text>
  </svg>
  <div class="abs pointer"></div>
  <h3 class="abs display heading" style="left:152px;top:336px">Doluptam as quid magnihi cabore rnonse plitius<br>etaut eturi reius, tempor si occaese</h3>
  <div class="abs rule" style="left:152px;top:370px;width:347px"></div>
  <p class="abs copy" style="left:152px;top:377px;width:347px">Hicienec uptaqui aectam acepra sunt officia dolumquis dolecae comnis untus demiste nes rehentem reperro volese eicidername net, consed mi, tem asimporeiur alistintenta apicitia porerum quid mi, corporiati aceatenate voloratum etur accum ut is sectem.</p>

  <h3 class="abs display heading" style="left:18px;top:447px">Doluptam as quid magni cabore<br>re nonse plitius cabore rnonse</h3>
  <p class="abs copy" style="left:18px;top:488px;width:234px">Hicienec uptaqui aectam acepra sunt officia dolumquis dolecae comnis untus demquia nes rehentem reperro volese eicidername net, consed mi, tem asimporeiur alistint apicitia porerum quid mi, corporiati aceatenate voloratum etur accum entem reperro volese eicidername. Dolecae comnis untus demquia nes rehentem reperrosi.</p>

  <div class="abs" style="left:258px;top:447px;width:1px;height:118px;background:var(--red)"></div>
  <p class="abs display completion" style="left:266px;top:447px"><span class="small" style="font-size:13px">Completion</span><span class="big" style="font-size:24px">% Rate</span></p>

  <svg class="abs chart-svg" style="left:0;top:0" width="514" height="729" role="img" aria-label="Completion rate by month: 25, 5, 45, 30, 35">
    <line x1="258" y1="563" x2="500" y2="563" stroke="var(--ink)" stroke-width="1"/>
    <polyline points="258,538 304,515 345,543 388,464 418,505 461,486 499,505" fill="none" stroke="var(--ink)" stroke-width="1.2"/>
    <g font-size="10" font-weight="600" fill="#fff" text-anchor="middle">
      <circle cx="304" cy="515" r="9" fill="var(--ink)" stroke="var(--red)" stroke-width="2.5"/><text x="304" y="519">25</text>
      <circle cx="345" cy="543" r="9" fill="var(--ink)" stroke="var(--red)" stroke-width="2.5"/><text x="345" y="547">5</text>
      <circle cx="388" cy="464" r="9" fill="var(--ink)" stroke="var(--red)" stroke-width="2.5"/><text x="388" y="468">45</text>
      <circle cx="418" cy="505" r="9" fill="var(--ink)" stroke="var(--red)" stroke-width="2.5"/><text x="418" y="509">30</text>
      <circle cx="461" cy="486" r="9" fill="var(--ink)" stroke="var(--red)" stroke-width="2.5"/><text x="461" y="490">35</text>
    </g>
    <g font-size="5.5" fill="var(--ink)" text-anchor="middle">
      <text x="262" y="572">JAN</text><text x="282" y="572">FEB</text><text x="303" y="572">MAR</text><text x="324" y="572">APR</text><text x="345" y="572">MAY</text><text x="366" y="572">JUN</text><text x="388" y="572">JUL</text><text x="409" y="572">AUG</text><text x="430" y="572">SEP</text><text x="451" y="572">OCT</text><text x="472" y="572">NOV</text><text x="494" y="572">DEC</text>
    </g>
  </svg>

  <p class="abs display www">WWW</p>
  <p class="abs display urls-label">Sample URL’s</p>
  <div class="abs rule" style="left:18px;top:650px;width:98px"></div>
  <ul class="abs url-list">
    <li>www.reelpulsemedia.com</li>
    <li>www.framecastlab.net</li>
    <li>www.viewtrailstudio.com</li>
    <li>www.motion-ledgergroup.com</li>
  </ul>
  <div class="abs extra-box display">Adicional<br>informations</div>
</section>

</body>
</html>
```